Tarjetas de visita para empresa de aluminio

Empresa con mas de 40 años vendiendo perfiles de aluminio.
Somos fábrica y almacén, queremos renovar la tarjeta de presentación de nuestros comerciales dando una imgen innovadora y tecnógica mezclado con la calidez del respeto al medio ambiente.
Añado el logo de la empresa y actual cara trasera de la tarjeta de visita, el logo es el simbolo WM y la marca TRAVENIC EXTRUSION, la frase 2extrusion y lacado de aluminio" debe cambiarse por "Diseño, extrusión, lacado, anodizado y mecanizado de precisión de aluminio" o en su defecto incluir todos esos servicios que hacemos o una frase mas pegadiza.

We are an aluminium factory, we produce and stock profiles of aluminium.
we want to renew visit card of our sellers, we are looking for something that show innovation, tecnology and environment respect.
Upload our actual logo and back of visit card, logo WM and brand TRAVENIC EXTRUSION must be keept.
Text "Extrusion y lacado de aluminio" must be changed for "Diseño, extrusion, lacado, anodizado y mecanizado de precisión de aluminio" or something like that

```html
<!DOCTYPE html>
<html lang="es">
<head>
<meta charset="utf-8">
<title>Tarjeta de visita · Aluminios Travenic</title>
<link href="https://fonts.googleapis.com/css2?family=Oswald:wght@600&family=Roboto:wght@500;700&display=swap" rel="stylesheet">
<style>
  :root {
    --backdrop: #adadad;
    --card-white: #ffffff;
    --navy: #243f8e;
    --navy-deep: #062b63;
    --navy-mid: #123d7c;
    --navy-light: #2a5ea3;
    --rule: #1f3a6e;
    --ink-grey: #5a5a5a;
    --brand-grey: #6b6b6b;
    --chrome-blue: #bcd6f4;
  }
  * { margin: 0; padding: 0; box-sizing: border-box; }
  html, body { width: 1200px; height: 1000px; overflow: hidden; }
  body { background: var(--backdrop); position: relative; font-family: 'Roboto', sans-serif; }

  .card {
    position: absolute;
    left: 294px;
    width: 613px;
    height: 352px;
    border-radius: 26px;
    overflow: hidden;
  }
  .card--front { top: 125px; background: var(--card-white); }
  .card--back { top: 537px; background: var(--navy-deep); }

  .front-brand-dot {
    position: absolute;
    right: 68px; top: 30px;
    width: 34px; height: 34px;
    border-radius: 50%;
    background: var(--brand-grey);
    opacity: 0.35;
  }
  .front-brand {
    position: absolute;
    right: 40px; top: 70px;
    font-weight: 500;
    font-size: 13px;
    line-height: 16px;
    letter-spacing: 0.5px;
    color: var(--brand-grey);
    white-space: nowrap;
  }

  .person-name {
    position: absolute;
    left: 40px; top: 194px;
    font-family: 'Oswald', sans-serif;
    font-weight: 600;
    font-size: 24px;
    line-height: 30px;
    color: var(--navy);
    letter-spacing: 0.3px;
  }
  .person-role {
    position: absolute;
    left: 40px; top: 225px;
    font-weight: 700;
    font-size: 17px;
    line-height: 20px;
    color: var(--ink-grey);
  }
  .divider {
    position: absolute;
    left: 40px; top: 253px;
    width: 527px; height: 2px;
    background: var(--rule);
  }
  .contact-line {
    position: absolute;
    left: 38px;
    display: flex; align-items: center; gap: 9px;
    font-weight: 700;
    font-size: 17px;
    line-height: 20px;
    color: var(--ink-grey);
  }
  .contact-line--phone { top: 283px; }
  .contact-line--mail { top: 306px; }
  .contact-line svg { width: 18px; height: 18px; flex: none; }
  .website {
    position: absolute;
    right: 46px; top: 306px;
    font-weight: 700;
    font-size: 17px;
    line-height: 20px;
    color: var(--ink-grey);
  }

  .back-pattern {
    position: absolute; inset: 0;
    background:
      radial-gradient(ellipse at 100% 40%, rgba(120,170,230,0.35) 0%, rgba(120,170,230,0) 60%),
      linear-gradient(90deg, var(--navy-deep) 0%, var(--navy-deep) 25%, var(--navy-mid) 65%, var(--navy-light) 100%);
  }
  .back-brand {
    position: absolute;
    left: 233px; top: 263px;
    font-weight: 500;
    font-size: 25px;
    line-height: 30px;
    letter-spacing: 1.3px;
    color: var(--chrome-blue);
    white-space: nowrap;
  }
</style>
</head>
<body>

  <section class="card card--front">
    <div class="front-brand-dot"></div>
    <div class="front-brand">ALUMINIOS TRAVENIC</div>

    <h1 class="person-name">MARCOS RÍOS DELGADO</h1>
    <p class="person-role">Comercial</p>
    <div class="divider"></div>

    <p class="contact-line contact-line--phone">
      <svg viewBox="0 0 18 18" aria-hidden="true">
        <rect x="4.5" y="1" width="9" height="16" rx="1.6" fill="none" stroke="#243f8e" stroke-width="1.6"/>
        <line x1="7.5" y1="14.2" x2="10.5" y2="14.2" stroke="#243f8e" stroke-width="1.4"/>
      </svg>
      955 000 142
    </p>
    <p class="contact-line contact-line--mail">
      <svg viewBox="0 0 18 18" aria-hidden="true">
        <rect x="1" y="3.5" width="16" height="11" fill="none" stroke="#243f8e" stroke-width="1.4"/>
        <polyline points="1,3.5 9,10 17,3.5" fill="none" stroke="#243f8e" stroke-width="1.4"/>
        <line x1="1" y1="14.5" x2="7" y2="8.5" stroke="#243f8e" stroke-width="1.2"/>
        <line x1="17" y1="14.5" x2="11" y2="8.5" stroke="#243f8e" stroke-width="1.2"/>
      </svg>
      info@travenic.es
    </p>
    <p class="website">www.travenic.es</p>
  </section>

  <section class="card card--back">
    <div class="back-pattern" role="img" aria-label="Patrón decorativo repetido del símbolo de la marca en efecto metálico sobre azul marino, más brillante hacia la derecha"></div>
    <div class="back-brand">ALUMINIOS TRAVENIC</div>
  </section>

</body>
</html>
```